Brochure Design for logistics company

Hi
We are a logistics company helping our clients in seafreight, airfreight and roadfreight.
Our current 4 pages brochure is outdated. We hope to refresh and make it more professional and eye-catching for our digital and print marketing.

```html
<!DOCTYPE html>
<html lang="en">
<head>
<meta charset="utf-8">
<title>KRV Logistics Brochure</title>
<link href="https://fonts.googleapis.com/css2?family=Roboto:wght@300;400;500;700;900&display=swap" rel="stylesheet">
<style>
:root{
  --red:#e41d24;
  --black:#0d0d0d;
  --grey:#8a8a8a;
  --text:#333;
  --paper:#fff;
  --bg:#fff;
}
html,body{margin:0;padding:0;overflow:hidden;background:var(--bg);}
.canvas{position:relative;width:693px;height:1200px;overflow:hidden;background:var(--bg);font-family:"Roboto",sans-serif;}
.page{position:absolute;width:252px;height:356px;background:var(--paper);box-shadow:0 2px 4px rgba(0,0,0,.25);}
.page svg{display:block;width:100%;height:100%;}
.cover{left:196px;top:2px;}
.about{left:71px;top:392px;}
.services{left:355px;top:392px;}
.back{left:230px;top:802px;}
text{font-family:"Roboto",sans-serif;}
.brand{font-weight:500;fill:var(--black);}
.h-red{fill:var(--red);font-weight:700;}
.body{fill:var(--text);font-size:3.6px;}
.item{fill:var(--text);font-size:3.6px;}
.panel-text{fill:#fff;font-size:3.6px;}
</style>
</head>
<body>
<div class="canvas">

  <!-- Front cover -->
  <section class="page cover">
    <svg viewBox="0 0 335 475">
      <rect class="brand-mark" x="196" y="57" width="10" height="10" fill="var(--red)"/>
      <text class="brand" x="210" y="68" font-size="15">KRV Logistics</text>
      <polygon points="0,52 190,148 45,240 0,215" fill="var(--black)"/>
      <polygon points="50,130 120,182 50,235" fill="var(--red)"/>
      <polygon role="img" aria-label="Photo of a truck hauling a blue shipping container under a blue sky" points="45,240 190,148 275,195 275,330" fill="url(#skyTruck)"/>
      <polygon points="275,188 335,215 335,372 275,345" fill="var(--black)"/>
      <defs>
        <linearGradient id="skyTruck" x1="0" y1="0" x2="0" y2="1">
          <stop offset="0" stop-color="#4a9be0"/>
          <stop offset=".55" stop-color="#2c5e9e"/>
          <stop offset="1" stop-color="#8d8d8d"/>
        </linearGradient>
      </defs>
      <text x="44" y="345" font-size="32" font-weight="300" fill="var(--grey)">WE MAKE</text>
      <text x="44" y="386" font-size="34" font-weight="700" fill="var(--red)">LOGISTICS</text>
      <text x="44" y="425" font-size="34" font-weight="700" fill="var(--black)">SIMPLE</text>
      <rect x="30" y="439" width="95" height="2.5" fill="var(--red)"/>
      <rect x="125" y="439" width="92" height="2.5" fill="var(--black)"/>
    </svg>
  </section>

  <!-- Inside left: about -->
  <section class="page about">
    <svg viewBox="0 0 335 475">
      <defs>
        <linearGradient id="port" x1="0" y1="0" x2="0" y2="1">
          <stop offset="0" stop-color="#7fb3e6"/>
          <stop offset=".5" stop-color="#6a8fb0"/>
          <stop offset="1" stop-color="#8a5a45"/>
        </linearGradient>
      </defs>
      <polygon role="img" aria-label="Photo of a container port with cranes and a loaded cargo ship" points="0,0 335,0 335,275 0,225" fill="url(#port)"/>
      <polygon points="0,115 115,176 0,228" fill="var(--red)"/>
      <text class="body" x="24" y="260"><tspan fill="var(--red)" font-weight="700">KRV Logistics</tspan> has been a key player in global transport and freight forwarding for more than 10 years.</text>
      <text class="body" x="24" y="272">Based in Sydney, Australia, KRV Logistics is a modern, dynamic, innovative company that always meets each</text>
      <text class="body" x="24" y="277">client's needs with its tailor-made solutions and personal touch.</text>
      <text class="body" x="24" y="289">With our strong logistics network and industry partnerships at home and abroad, along with our experience</text>
      <text class="body" x="24" y="294">and professionalism, KRV Logistics can offer the most cost-effective solutions and services to our clients.</text>
      <text class="h-red" x="26" y="318" font-size="7.5">OUR COMMITMENTS</text>

      <circle cx="34" cy="334" r="6" fill="var(--black)"/>
      <text class="h-red" x="44" y="336" font-size="4.6">Expertise</text>
      <text class="body" x="26" y="350">KRV Logistics is a well-established and experienced</text>
      <text class="body" x="26" y="355">international freight forwarder, especially with the</text>
      <text class="body" x="26" y="360">Asian countries. With strong links and partnerships</text>
      <text class="body" x="26" y="365">in China, South Korea, Japan, Thailand and India,</text>
      <text class="body" x="26" y="370">KRV Logistics strives to achieve seamless and</text>
      <text class="body" x="26" y="375">effective results for all our clients.</text>

      <circle cx="203" cy="334" r="6" fill="var(--black)"/>
      <text class="h-red" x="213" y="336" font-size="4.6">Solution Service</text>
      <text class="body" x="195" y="350">At KRV Logistics, we provide our clients with the</text>
      <text class="body" x="195" y="355">highest standard of service, not only being flexible</text>
      <text class="body" x="195" y="360">and understanding, but we also always go the extra</text>
      <text class="body" x="195" y="365">mile to achieve the best outcome. There is no issue</text>
      <text class="body" x="195" y="370">too big for us. We listen to each client's needs</text>
      <text class="body" x="195" y="375">and make every effort to provide workable and</text>
      <text class="body" x="195" y="380">effective solutions.</text>

      <circle cx="34" cy="396" r="6" fill="var(--black)"/>
      <text class="h-red" x="44" y="398" font-size="4.6">Reduce Cost</text>
      <text class="body" x="26" y="412">Time is money! No client is opposed to cost saving</text>
      <text class="body" x="26" y="417">and increasing profit margin. With our own</text>
      <text class="body" x="26" y="422">technology, KRV Logistics uses smart algorithms</text>
      <text class="body" x="26" y="427">to determine and select the most suitable carriers</text>
      <text class="body" x="26" y="432">and warehouses to minimise cost and time.</text>

      <rect role="img" aria-label="Photo of hands holding coloured blocks labelled customs" x="196" y="402" width="117" height="50" fill="#b5504a"/>
      <text x="240" y="431" font-size="5" font-weight="700" fill="#fff">CUSTOMS</text>
      <text class="body" x="26" y="452">www.krvfreight.com.au/</text>
    </svg>
  </section>

  <!-- Inside right: services -->
  <section class="page services">
    <svg viewBox="0 0 335 475">
      <defs>
        <linearGradient id="yard" x1="0" y1="0" x2="1" y2="1">
          <stop offset="0" stop-color="#fff" stop-opacity="0"/>
          <stop offset=".35" stop-color="#9fb7cf"/>
          <stop offset="1" stop-color="#c9a14a"/>
        </linearGradient>
        <g id="tick"><circle r="1.8" fill="none" stroke="#666" stroke-width=".5"/><path d="M-.8,0 L-.2,.7 L.9,-.7" fill="none" stroke="#666" stroke-width=".5"/></g>
        <g id="tickW"><circle r="1.8" fill="none" stroke="#fff" stroke-width=".5"/><path d="M-.8,0 L-.2,.7 L.9,-.7" fill="none" stroke="#fff" stroke-width=".5"/></g>
      </defs>
      <polygon role="img" aria-label="Photo of a worker in a hard hat and hi-vis vest with a radio, overseeing trucks at a container yard" points="100,415 335,415 335,250 200,250" fill="url(#yard)"/>
      <text class="h-red" x="24" y="27" font-size="7.5">OUR COMMITMENTS</text>

      <rect x="222" y="45" width="113" height="227" fill="var(--red)"/>
      <text x="230" y="59" font-size="5.2" font-weight="700" fill="#fff">Our dedicated team work</text>
      <text x="230" y="66" font-size="5.2" font-weight="700" fill="#fff">closely with clients to:</text>
      <g class="panel-text">
        <use href="#tickW" x="232" y="80"/><text x="238" y="81">Manage both domestic and</text><text x="238" y="85">international shipping.</text>
        <use href="#tickW" x="232" y="98"/><text x="238" y="99">Access to a broad range of</text><text x="238" y="103">transportation service.</text>
        <use href="#tickW" x="232" y="116"/><text x="238" y="117">Oversee customs regulations</text><text x="238" y="121">and compliance.</text>
        <use href="#tickW" x="232" y="134"/><text x="238" y="135">Identify potential time and</text><text x="238" y="139">cost saving.</text>
        <use href="#tickW" x="232" y="152"/><text x="238" y="153">Document and simplify the</text><text x="238" y="157">logistics process for client.</text>
        <use href="#tickW" x="232" y="170"/><text x="238" y="171">Constant and clear communi-</text><text x="238" y="175">cation.</text>
        <use href="#tickW" x="232" y="188"/><text x="238" y="189">Consult and facilitate idea</text><text x="238" y="193">generation with client.</text>
        <use href="#tickW" x="232" y="206"/><text x="238" y="207">Liaise between allocated</text><text x="238" y="211">carriers and delivery sites.</text>
        <use href="#tickW" x="232" y="224"/><text x="238" y="225">Resolve disputes raised by</text><text x="238" y="229">client and carriers.</text>
        <use href="#tickW" x="232" y="242"/><text x="238" y="243">And anything else needed to</text><text x="238" y="247">add value to the business</text><text x="238" y="251">logistics requirements.</text>
      </g>

      <circle cx="33" cy="51" r="9" fill="var(--black)"/>
      <text class="h-red" x="48" y="49" font-size="4.2">INTERNATIONAL</text>
      <text class="h-red" x="48" y="54" font-size="4.2">FREIGHT (FCL &amp;LCL)</text>
      <g class="item">
        <use href="#tick" x="29" y="73"/><text x="34" y="74">Import &amp; Export Services</text>
        <use href="#tick" x="29" y="85"/><text x="34" y="86">Air Freight Forwarding</text>
        <use href="#tick" x="29" y="97"/><text x="34" y="98">Ocean Freight Forwarding</text>
        <use href="#tick" x="29" y="109"/><text x="34" y="110">Customs Clearance &amp;</text><text x="34" y="114">Quarantine</text>
        <use href="#tick" x="29" y="127"/><text x="34" y="128">Global Trade Compliance</text>
      </g>

      <circle cx="136" cy="51" r="9" fill="var(--black)"/>
      <text class="h-red" x="151" y="49" font-size="4.2">DOMESTIC</text>
      <text class="h-red" x="151" y="54" font-size="4.2">FREIGHT</text>
      <g class="item">
        <use href="#tick" x="131" y="73"/><text x="136" y="74">Dry Van, Flat Bed &amp;</text><text x="136" y="78">Refrigerated</text>
        <use href="#tick" x="131" y="91"/><text x="136" y="92">Rail &amp; Intermodal Drayage</text><text x="136" y="96">&amp; Port</text><text x="136" y="100">Services</text>
        <use href="#tick" x="131" y="115"/><text x="136" y="116">Domestic Air, Ocean &amp;</text><text x="136" y="120">Road</text>
      </g>

      <circle cx="33" cy="169" r="9" fill="var(--black)"/>
      <text class="h-red" x="48" y="167" font-size="4.2">INDUSTRY</text>
      <text class="h-red" x="48" y="172" font-size="4.2">SOLUTION</text>
      <g class="item">
        <use href="#tick" x="29" y="192"/><text x="34" y="193">Food &amp; Beverage</text>
        <use href="#tick" x="29" y="204"/><text x="34" y="205">Furniture</text>
        <use href="#tick" x="29" y="216"/><text x="34" y="217">E-Commerce</text>
        <use href="#tick" x="29" y="228"/><text x="34" y="229">Technology</text>
        <use href="#tick" x="29" y="240"/><text x="34" y="241">Construction &amp; Building</text>
        <use href="#tick" x="29" y="252"/><text x="34" y="253">Automotive</text>
        <use href="#tick" x="29" y="264"/><text x="34" y="265">Machinery (Light &amp; Heavy)</text>
      </g>

      <circle cx="136" cy="169" r="9" fill="var(--black)"/>
      <text class="h-red" x="151" y="167" font-size="4.2">PROJECT</text>
      <text class="h-red" x="151" y="172" font-size="4.2">CARGO</text>
      <g class="item">
        <use href="#tick" x="131" y="192"/><text x="136" y="193">Breakbulk, Oversized &amp;</text><text x="136" y="197">Heavy-Lift</text>
        <use href="#tick" x="131" y="210"/><text x="136" y="211">Warehousing &amp; Crating</text>
        <use href="#tick" x="131" y="222"/><text x="136" y="223">Vendor Management</text>
        <use href="#tick" x="131" y="234"/><text x="136" y="235">On-Site Delivery Scheduling</text>
      </g>

      <circle cx="33" cy="306" r="9" fill="var(--black)"/>
      <text class="h-red" x="48" y="304" font-size="4.2">WAREHOUSING &amp;</text>
      <text class="h-red" x="48" y="309" font-size="4.2">FULFILLMENT</text>
      <g class="item">
        <use href="#tick" x="29" y="328"/><text x="34" y="329">Inbound &amp; Outbound</text><text x="34" y="333">Process</text>
        <use href="#tick" x="29" y="346"/><text x="34" y="347">Inventory Management</text>
        <use href="#tick" x="29" y="358"/><text x="34" y="359">Pick, Pack and Ship</text>
        <use href="#tick" x="29" y="370"/><text x="34" y="371">Order Entry &amp; Reporting</text>
        <use href="#tick" x="29" y="382"/><text x="34" y="383">Return Management</text>
      </g>

      <g class="partner-badges">
        <rect x="30" y="420" width="40" height="40" rx="6" fill="#d7dbe6"/>
        <rect x="95" y="420" width="40" height="40" rx="6" fill="#cfe0f2"/>
        <rect x="160" y="425" width="70" height="30" rx="4" fill="#f4e1a6"/>
        <circle cx="287" cy="440" r="18" fill="#cfe0f2"/>
      </g>
    </svg>
  </section>

  <!-- Back cover -->
  <section class="page back">
    <svg viewBox="0 0 335 475">
      <polygon points="0,0 222,0 0,110" fill="var(--red)"/>
      <circle cx="85" cy="75" r="50" fill="#fff"/>
      <circle role="img" aria-label="Photo of parcels and a small delivery truck" cx="85" cy="75" r="45" fill="#b89a74"/>
      <rect x="185" y="57" width="10" height="10" fill="var(--red)"/>
      <text class="brand" x="199" y="68" font-size="15">KRV Logistics</text>
      <polygon points="0,325 335,180 335,380 125,475 0,475" fill="var(--black)"/>
      <text x="117" y="305" font-size="10" font-weight="700" fill="var(--red)">CALL US TODAY</text>
      <rect x="117" y="313" width="25" height="1.5" fill="var(--red)"/>
      <g fill="none" stroke="#fff" stroke-width=".8">
        <circle cx="124" cy="328" r="4.5"/>
        <path d="M122,326 q0,4 4,4" />
        <circle cx="124" cy="347" r="4.5"/>
        <rect x="121.5" y="345.5" width="5" height="3.4"/>
        <circle cx="124" cy="364" r="4.5"/>
        <ellipse cx="124" cy="364" rx="1.8" ry="4.5"/>
        <circle cx="124" cy="382" r="4.5"/>
        <circle cx="124" cy="381" r="1.3"/>
      </g>
      <g fill="#fff">
        <text x="136" y="332" font-size="9">+61 2 5550 1234</text>
        <text x="136" y="351" font-size="7.5">hello@krvfreight.com.au</text>
        <text x="136" y="368" font-size="7.5">www.krvfreight.com.au</text>
        <text x="136" y="383" font-size="5.6">24/8 Harbour Road</text>
        <text x="136" y="390" font-size="5.6">Portside NSW 2099</text>
        <text x="136" y="397" font-size="5.6">NSW AUSTRALIA</text>
      </g>
    </svg>
  </section>

</div>
</body>
</html>
```